Business Card Design Project

use presentation folder design and my logo and make 4 over 4 business cards

Industry/Entity Type

Business

Requirements
Must have
• use the design from my presentation folder and put my logo on it

Name
Title
phone
fax
email

```html
<!DOCTYPE html>
<html lang="en">
<head>
<meta charset="utf-8">
<title>Harborlight Counseling – Business Card</title>
<link rel="stylesheet" href="https://fonts.googleapis.com/css2?family=Questrial&family=Crimson+Text:wght@400;600&display=swap">
<style>
  :root {
    --page-bg: #ece7df;
    --card-white: #ffffff;
    --ink: #1d1d1d;
    --brown: #7a4520;
    --teal-deep: #05828d;
    --teal-mid: #0aa0ad;
    --teal-light: #35bcc6;
    --warm-photo-a: #e7b99a;
    --warm-photo-b: #c9874f;
    --family-photo-a: #f0ede9;
    --family-photo-b: #c9b29b;
  }
  * { box-sizing: border-box; margin: 0; padding: 0; }
  html, body { width: 1200px; height: 1000px; overflow: hidden; }
  body { background: var(--page-bg); position: relative; font-family: "Crimson Text", serif; }

  .card {
    position: absolute;
    width: 640px;
    height: 366px;
    border-radius: 4px;
    overflow: hidden;
    box-shadow: 0 6px 18px rgba(0,0,0,0.18);
  }

  .brand {
    position: absolute;
    display: flex;
    align-items: center;
    gap: 10px;
  }
  .brand-dot {
    width: 30px; height: 30px; border-radius: 50%;
    background: var(--brown);
    flex: none;
  }
  .brand-name {
    font-family: "Crimson Text", serif;
    font-weight: 600;
    font-size: 30px;
    line-height: 1;
    color: var(--brown);
    white-space: nowrap;
  }

  /* Front */
  .card-front { left: 80px; top: 90px; background: var(--card-white); }
  .card-front .brand { right: 34px; top: 36px; }

  .holder-name {
    position: absolute; left: 42px; top: 106px;
    font-family: "Questrial", sans-serif;
    font-weight: 400;
    font-size: 38px; line-height: 1.1; color: var(--ink); letter-spacing: 0.3px;
  }
  .holder-title {
    position: absolute; left: 46px; top: 156px;
    font-size: 18px; line-height: 1.2; color: var(--ink);
  }
  .photo-group {
    position: absolute; left: 0; top: 222px;
    width: 312px; height: 94px;
    background: linear-gradient(100deg, var(--warm-photo-b), var(--warm-photo-a) 55%, #f3e3d6);
  }
  .photo-family {
    position: absolute; left: 300px; top: 192px;
    width: 290px; height: 124px;
    border-radius: 0 22px 22px 0;
    background: linear-gradient(90deg, var(--family-photo-a), var(--family-photo-b) 60%, var(--family-photo-a));
  }
  .side-tab {
    position: absolute; right: -20px; top: 184px;
    width: 40px; height: 118px;
    border-radius: 18px;
    background: var(--brown);
  }
  .contact-line {
    position: absolute; left: 42px; top: 330px;
    font-size: 16.5px; line-height: 1.2; color: var(--ink);
    white-space: nowrap;
  }

  /* Back */
  .card-back { left: 480px; top: 560px; }
  .back-surface {
    position: absolute; inset: 0;
    background: linear-gradient(160deg, var(--teal-light), var(--teal-mid) 50%, var(--teal-deep));
  }
  .back-band {
    position: absolute; left: 190px; top: 108px;
    width: 450px; height: 126px;
    background: var(--card-white);
    border-radius: 26px 0 0 26px;
  }
  .card-back .brand { left: 40px; top: 48px; }
</style>
</head>
<body>

  <section class="card card-front" aria-label="Business card front">
    <div class="brand">
      <span class="brand-dot"></span>
      <span class="brand-name">Harborlight Counseling</span>
    </div>

    <h1 class="holder-name">Daniel Marsh</h1>
    <p class="holder-title">Health Consultant</p>

    <div class="photo-group" role="img" aria-label="Photo of three smiling young women"></div>
    <div class="photo-family" role="img" aria-label="Photo of a smiling family: father, son and mother"></div>
    <div class="side-tab"></div>

    <p class="contact-line">Ph: 041 2288 317 | Fax: 041 2288 318 | daniel@mailbox.example</p>
  </section>

  <section class="card card-back" aria-label="Business card back">
    <div class="back-surface" role="img" aria-label="Teal background with soft flowing wave pattern"></div>
    <div class="back-band">
      <div class="brand">
        <span class="brand-dot"></span>
        <span class="brand-name">Harborlight Counseling</span>
      </div>
    </div>
  </section>

</body>
</html>
```